Letterhead for Midwest Law Firm

Our law firm does estate planning and trust administration in Wisconsin and Illinois. We recently obtained a new logo and need to incorporate it into new stationary. The stationary needs to list out the attorneys at the firm, but we will want 3 variations, one with three attorneys, one with six, and one with six plus the names of states where each is licensed to practice (possibly as an asterisk with notation somewhere towards bottom of page. As with most traditional law practices, letterhead should be conservative and convey predictability and reliability. We view our brand as being primarily reliability, with prestige as a secondary element. We are upmarket, but would like to avoid seeming pretentious or "slick". We are a smaller firm with a personal touch.

Target Market(s)

Affluent Midwestern Americans approaching at or approaching retirement age.

Industry/Entity Type

Legal

Font styles to use
Serif
Sans Serif

Requirements
Must have
• Must use our logo. Must comply with Northgate Counsel Guild Ethics rules: https://www.quarvenlex.org/rules/offices/docs/plmtk41annotated.pdf. Must be conventional. Must list names of attorneys and provide contact information for firm. Note that we are asking for three designs with very minor variations. Also, designer must provide letterhead in a format that is industry-standard for stationary printers.
Nice to have
• We would appreciate an alternate version that will look reasonable when printed on a black-and-white printer. Designer can use judgment as to whether to have use grayscale, black/white, or something in between.
Should not have
• No "motto" or "visit our website" extraneous materials. putting the website address somewhere is fine, but overall there is a lot of required text, and we'd like to not appear cluttered.

```html
<!DOCTYPE html>
<html lang="en">
<head>
<meta charset="utf-8">
<title>Halvorsen &amp; Pryce LLP — Letterhead</title>
<link href="https://fonts.googleapis.com/css2?family=Libre+Baskerville:wght@700&family=Lato:wght@400;700&family=Montserrat:wght@300;400;700&family=PT+Sans+Narrow&display=swap" rel="stylesheet">
<style>
  :root{
    --navy:#2a2a40;
    --gold:#f4b02a;
    --ink:#555659;
    --ink-soft:#6a6b6e;
    --backdrop:#d6d6d6;
    --paper:#ffffff;
  }
  *{box-sizing:border-box;margin:0;padding:0}
  html,body{width:1056px;height:1200px;overflow:hidden;background:var(--backdrop)}
  .letterhead{
    position:absolute;left:118px;top:20px;width:820px;height:1160px;
    background:var(--paper);overflow:hidden;
    box-shadow:0 6px 24px rgba(0,0,0,.18);
  }
  .firm-mark{position:absolute;left:77px;top:52px;width:198px;text-align:center}
  .firm-mark__dot{display:block;width:40px;height:40px;border-radius:50%;background:var(--gold);margin:0 auto 18px}
  .firm-mark__name{font-family:"Libre Baskerville",serif;font-weight:700;font-size:17px;color:var(--navy);white-space:nowrap}
  .firm-mark__rule{height:2px;background:var(--gold);margin-top:10px}
  .header-rule{position:absolute;left:77px;top:168px;width:598px;height:1.5px;background:var(--navy)}
  .staff{position:absolute;right:78px;top:52px;text-align:right;list-style:none;font-family:"Lato",sans-serif}
  .staff__item{margin-bottom:8px}
  .staff__name{display:block;font-weight:700;font-size:16.5px;color:var(--navy);line-height:19px}
  .staff__role{display:block;font-size:13.5px;color:var(--gold);line-height:16px}
  .letter{position:absolute;left:77px;top:388px;width:665px;color:var(--ink)}
  .letter__date{font-family:"Montserrat",sans-serif;font-weight:300;font-size:18px}
  .letter__recipient{font-family:"Montserrat",sans-serif;font-weight:700;font-size:28px;margin-top:8px;letter-spacing:-.2px}
  .letter__title{font-family:"Montserrat",sans-serif;font-weight:300;font-size:18px;margin-top:4px}
  .letter__body{margin-top:44px;font-family:"PT Sans Narrow",sans-serif;font-size:17.5px;letter-spacing:.15px;line-height:28.5px;text-align:justify}
  .letter__body p+p{margin-top:28.5px}
  .letter__closing{margin-top:56px;font-family:"PT Sans Narrow",sans-serif;font-size:18px}
  .signature{width:86px;height:56px;margin-top:18px;border-radius:4px;background:linear-gradient(135deg,#ececf0,#dcdce4)}
  .contact{position:absolute;left:77px;top:1070px;display:flex;font-family:"Montserrat",sans-serif;font-size:14.5px;color:var(--ink-soft);line-height:22px}
  .contact__phones div{display:flex;align-items:center;gap:8px}
  .contact__divider{width:1.5px;height:36px;background:var(--navy);margin:4px 16px 0 16px}
  .footer-band{position:absolute;left:0;bottom:0;width:820px;height:32px}
  .footer-band__url{position:absolute;right:23px;bottom:9px;font-family:"Lato",sans-serif;font-size:13px;color:#fff}
</style>
</head>
<body>
<main class="letterhead">
  <div class="firm-mark">
    <span class="firm-mark__dot"></span>
    <div class="firm-mark__name">Halvorsen &amp; Pryce LLP</div>
    <div class="firm-mark__rule"></div>
  </div>

  <ul class="staff">
    <li class="staff__item"><span class="staff__name">EDWIN C. HALVORSEN</span><span class="staff__role">Attorney</span></li>
    <li class="staff__item"><span class="staff__name">MARTIN R. HALVORSEN</span><span class="staff__role">Attorney</span></li>
    <li class="staff__item"><span class="staff__name">CLAIRE M. DUNMORE</span><span class="staff__role">Paralegal</span></li>
  </ul>
  <div class="header-rule"></div>

  <article class="letter">
    <div class="letter__date">10 December, 2021</div>
    <div class="letter__recipient">DANIEL FOSTER</div>
    <div class="letter__title">Cheif Executive Officer</div>
    <div class="letter__body">
      <p>Contrary to popular belief, Lorem Ipsum is not simply random text. It has roots in a piece of classical Latin literature from 45 BC, making it over 2000 years old. Harold Brenneman, a Latin professor at Ashford-Linden College in Kentshire, looked up one of the more obscure Latin words, consectetur.</p>
      <p>Lorem Ipsum comes from sections 1.10.32 and 1.10.33 of "de Rebus Antiquis et Novis" (The Extremes of Good and Evil) by Varelius, written in 45 BC. This book is a treatise on the theory of ethics, very popular during the Renaissance. The first line of Lorem Ipsum.</p>
      <p>The standard chunk of Lorem Ipsum used since the 1500s is reproduced below for those interested.</p>
    </div>
    <div class="letter__closing">Best Regards</div>
    <div class="signature" role="img" aria-label="Handwritten signature"></div>
  </article>

  <div class="contact">
    <div class="contact__phones">
      <div>
        <svg width="12" height="12" viewBox="0 0 24 24" aria-hidden="true"><path fill="#2a2a40" d="M6.6 10.8a15.1 15.1 0 0 0 6.6 6.6l2.2-2.2c.3-.3.7-.4 1-.2 1.1.4 2.300.6 3.6.6.6 0 1 .4 1 1V20c0 .6-.4 1-1 1C10.6 21 3 13.4 3 4c0-.6.4-1 1-1h3.5c.6 0 1 .4 1 1 0 1.3.2 2.5.6 3.6.1.3 0 .7-.2 1z"/></svg>
        555-014-7200
      </div>
      <div>
        <svg width="12" height="12" viewBox="0 0 24 24" aria-hidden="true"><path fill="#2a2a40" d="M6 2h12v5H6zM3 8h18a2 2 0 0 1 2 2v7h-5v5H6v-5H1v-7a2 2 0 0 1 2-2zm5 8v4h8v-4z"/></svg>
        555-014-0391
      </div>
    </div>
    <div class="contact__divider"></div>
    <div class="contact__address">
      <div>218 W. Ashcombe Street, Suite 400</div>
      <div>Lakemont, WI&nbsp; 54999</div>
    </div>
  </div>

  <svg class="footer-band" viewBox="0 0 820 32" aria-hidden="true">
    <polygon points="0,7 557,7 552,13 0,13" fill="var(--gold)"/>
    <polygon points="0,21 547,21 571,0 820,0 820,32 0,32" fill="var(--navy)"/>
  </svg>
  <span class="footer-band__url">www.halvorsenprycellp.com</span>
</main>
</body>
</html>
```